Brisk Morsels
Business Card and Stationary Design
Brisk Morsels -
Creative Brief
Bright & Fun-filled
Gordon T Welham
Owner
41 Harlow Lane Millbrook Ridge, NJ 08637
Gord.Welham@postmailer.example
www.brisk-morsels.example
Looking for something simple, but eye-catching. Looking for a variety of different fonts/styles/backgrounds to achieve: -Seamless integration with the attached logo. -Backgrounds to enhance the "pop" of the logo. -Professional, but with a hint of fun. The Brisk Morsel will compete in the energy drink/shot industry (e.g. Tan Lynx and Nine Minute Vigor). We differentiate ourselves through superior taste and natural ingredients, creating a more satisfying experience for the energy consumer. Feel free to message me with any questions/concerns/comments.

```html
<!DOCTYPE html>
<html lang="en">
<head>
<meta charset="utf-8">
<title>Brisk Morsels – Business Card</title>
<link href="https://fonts.googleapis.com/css2?family=Open+Sans:wght@400;600;700&display=swap" rel="stylesheet">
<style>
  :root {
    --page: #ece8e3;
    --card: #ffffff;
    --brown: #7a4a22;
    --brown-dark: #5c3414;
    --tan: #c9954e;
    --orange: #f08a1c;
    --ink: #4a4a4a;
    --muted: #8a8a8a;
  }
  html, body {
    margin: 0;
    width: 1200px;
    height: 816px;
    overflow: hidden;
    background: var(--page);
    font-family: "Open Sans", Arial, sans-serif;
  }
  .canvas { position: relative; width: 1200px; height: 816px; }
  .card {
    position: absolute;
    width: 480px;
    height: 274px;
    background: var(--card);
    border-radius: 10px;
    overflow: hidden;
    box-shadow: 0 6px 18px rgba(60, 40, 20, 0.18);
  }
  .card-front { left: 80px; top: 270px; }
  .card-back { left: 640px; top: 350px; }
  .card-decor { position: absolute; inset: 0; }
  .brand {
    position: absolute;
    display: flex;
    align-items: center;
    gap: 8px;
    color: var(--brown);
    font-weight: 700;
    letter-spacing: 0.5px;
  }
  .brand-dot {
    width: 14px; height: 14px;
    border-radius: 50%;
    background: var(--orange);
  }
  .card-front .brand { left: 44px; top: 40px; font-size: 26px; }
  .card-back .brand { left: 0; right: 0; top: 112px; justify-content: center; font-size: 34px; }
  .card-back .brand-dot { width: 18px; height: 18px; }
  .holder { position: absolute; left: 280px; top: 46px; }
  .holder-name { color: var(--orange); font-weight: 700; font-size: 15px; }
  .holder-role { color: var(--muted); font-size: 10px; margin-top: 2px; }
  .contact {
    position: absolute;
    left: 44px; top: 160px;
    font-size: 10px;
    color: var(--ink);
    line-height: 1.45;
  }
  .contact-line { margin-top: 10px; }
  .label { color: var(--orange); }
  .sep { color: var(--muted); margin: 0 6px; }
  .web { color: var(--orange); margin-top: 2px; }
</style>
</head>
<body>
<main class="canvas">
  <section class="card card-front">
    <svg class="card-decor" viewBox="0 0 480 274" preserveAspectRatio="none" aria-hidden="true">
      <defs>
        <linearGradient id="band" x1="0" y1="0" x2="1" y2="0">
          <stop offset="0" stop-color="#5c3414"/>
          <stop offset="1" stop-color="#c9954e"/>
        </linearGradient>
      </defs>
      <path d="M430 0 H480 V274 H474 C470 160 460 70 430 0 Z" fill="url(#band)"/>
      <path d="M430 0 C460 70 470 160 474 274" fill="none" stroke="#f08a1c" stroke-width="4"/>
      <path d="M0 110 C12 180 20 235 70 256 L472 258 V274 H0 Z" fill="url(#band)"/>
      <path d="M0 110 C12 180 20 235 70 256 L472 258" fill="none" stroke="#f08a1c" stroke-width="2"/>
    </svg>
    <div class="brand"><span class="brand-dot"></span>Brisk Morsels</div>
    <div class="holder">
      <div class="holder-name">Gordon T Welham</div>
      <div class="holder-role">Owner</div>
    </div>
    <div class="contact">
      <div>41 Harlow Lane</div>
      <div>Millbrook Ridge, NJ 08637</div>
      <div class="contact-line"><span class="label">Cell</span> (555) 014-2290<span class="sep">|</span><span class="label">Email</span> Gord.Welham@postmailer.example</div>
      <div class="web">www.brisk-morsels.example</div>
    </div>
  </section>

  <section class="card card-back">
    <div class="brand"><span class="brand-dot"></span>Brisk Morsels</div>
  </section>
</main>
</body>
</html>
```